Tarrow Creek plumbing plumbing company business card design

Something sinilar to business card i upload it is my old business card design
And have a good watermark with the logo or majority of the logot in rhe background as watermark

Plumbing business similar to uploaded design with a nice watermark of the logo

Font styles to use
Script

Colors

Designer to choose colors to be used in the design.

```html
<!DOCTYPE html>
<html lang="en">
<head>
<meta charset="utf-8">
<title>Tarrow Creek Plumbing – Business Card</title>
<link rel="stylesheet" href="https://fonts.googleapis.com/css2?family=Open+Sans:wght@400;700&display=swap">
<style>
  :root {
    --page: #ffffff;
    --brand-blue: #0b7bc2;
    --ink-dark: #111418;
    --card-black: #000000;
    --text-light: #ffffff;
    --watermark: rgba(255, 255, 255, 0.12);
  }
  * { margin: 0; padding: 0; box-sizing: border-box; }
  html, body {
    width: 1200px;
    height: 1200px;
    overflow: hidden;
    background: var(--page);
    font-family: "Open Sans", Arial, sans-serif;
  }
  .sheet {
    position: relative;
    width: 1200px;
    height: 1200px;
  }
  .card {
    position: absolute;
    left: 200px;
    width: 801px;
    height: 457px;
    overflow: hidden;
  }
  .card--front { top: 116px; background: var(--brand-blue); color: var(--text-light); }
  .card--back  { top: 641px; background: var(--card-black); }

  .front-brand {
    position: absolute;
    left: 40px;
    top: 44px;
    font-size: 34px;
    font-weight: 700;
    line-height: 1.15;
    color: var(--ink-dark);
    letter-spacing: 0.2px;
  }
  .holder {
    position: absolute;
    right: 40px;
    top: 128px;
    text-align: right;
  }
  .holder__name { font-size: 29px; font-weight: 700; line-height: 1.2; }
  .holder__role { font-size: 27px; font-weight: 400; line-height: 1.4; margin-top: 2px; }

  .licence {
    position: absolute;
    left: 40px;
    top: 272px;
    font-size: 18px;
  }
  .contacts {
    position: absolute;
    left: 40px;
    top: 322px;
    list-style: none;
    font-size: 18px;
  }
  .contacts__item {
    display: flex;
    align-items: center;
    height: 36px;
  }
  .contacts__icon { width: 14px; height: 14px; fill: var(--text-light); }
  .contacts__divider { margin: 0 8px 0 7px; opacity: 0.9; }

  .watermark {
    position: absolute;
    right: -20px;
    bottom: -20px;
    width: 190px;
    height: 190px;
    background: var(--watermark);
    border-radius: 18px;
  }

  .back-brand {
    position: absolute;
    left: 0;
    right: 0;
    top: 50%;
    transform: translateY(-50%);
    text-align: center;
    font-size: 54px;
    font-weight: 700;
    color: var(--text-light);
    letter-spacing: 0.5px;
  }
</style>
</head>
<body>
<main class="sheet">
  <section class="card card--front" aria-label="Business card front">
    <div class="front-brand">Tarrow Creek<br>Plumbing</div>

    <div class="holder">
      <p class="holder__name">Dario Kellaway</p>
      <p class="holder__role">Director</p>
    </div>

    <p class="licence">Lic No. 498273c</p>

    <ul class="contacts">
      <li class="contacts__item">
        <svg class="contacts__icon" viewBox="0 0 24 24" aria-hidden="true"><path d="M6.6 10.8a15.1 15.1 0 0 0 6.6 6.6l2.2-2.2c.3-.3.7-.4 1-.2 1.1.4 2.3.6 3.6.6.6 0 1 .4 1 1V20c0 .6-.4 1-1 1A17 17 0 0 1 3 4c0-.6.4-1 1-1h3.5c.6 0 1 .4 1 1 0 1.3.2 2.5.6 3.6.1.3 0 .7-.2 1z"/></svg>
        <span class="contacts__divider">|</span>0412555078
      </li>
      <li class="contacts__item">
        <svg class="contacts__icon" viewBox="0 0 24 24" aria-hidden="true"><path d="M2 5h20v14H2z" opacity="1"/><path d="M2 5l10 7 10-7" fill="none" stroke="#0b7bc2" stroke-width="2"/></svg>
        <span class="contacts__divider">|</span>info@tarrowcreekplumbing.com
      </li>
      <li class="contacts__item">
        <svg class="contacts__icon" viewBox="0 0 24 24" aria-hidden="true"><circle cx="12" cy="12" r="10"/><path d="M2 12h20M12 2c3 3 3 17 0 20M12 2c-3 3-3 17 0 20" fill="none" stroke="#0b7bc2" stroke-width="1.6"/></svg>
        <span class="contacts__divider">|</span>tarrowcreekplumbing.com.au
      </li>
    </ul>

    <div class="watermark" aria-hidden="true"></div>
  </section>

  <section class="card card--back" aria-label="Business card back">
    <div class="back-brand">Tarrow Creek Plumbing</div>
  </section>
</main>
</body>
</html>
```